Business Card Design Project

We need a business card design for a management consultancy focused on financial innovation and digital money, run by experts from the Financial Services, Telecoms and Money Transfer industries.
Our products include services such as Mobile Payments, Mobile Money, Digital Wallets, Online Payments, Branchless Banking and more. We work with regulatory information, business plans, financial modelling, strategic planning, new products functional specification, new technologies evaluation, etc.
See company logo attached.
We would like to see 2 versions: one in portuguese and one in english (regarding data information). You can see below information needed (whenever there is a difference between the two versions, the first one is in english and the second one in portuguese).

Name
Position
Phone/ Tel: ++55-11-xxxx-xxxx
Cell/ Cel: ++55-11-9 xxxx-xxxx
Dr. Morvelo Tastran Av., 512 - Tower II - 16th floor / Avenida Dr. Morvelo Tastran, 512 - Torre II - 16o. andar
São Paulo - SP
07219-316 - Brazil/ 07219-316 - Brasil

Target Market(s)

Audience: C-level executives from banks, credit card companies, acquirers, IT developers, retailers

Industry/Entity Type

Financial

Requirements
Must have
• Must use the logo and information above. Front must have white background. Back side should have only logo.
Nice to have
• Back should be in another colour but if it seems too exxagerated, maintain back in white also.
Should not have
• Do not add other illustrations to the business card.

```html
<!DOCTYPE html>
<html lang="en">
<head>
<meta charset="utf-8">
<title>R Marlowe Management Consulting – Business Cards</title>
<link rel="stylesheet" href="https://fonts.googleapis.com/css2?family=Open+Sans:wght@400;600;700&display=swap">
<style>
  :root {
    --page-bg: #e9e7e4;
    --card-white: #ffffff;
    --navy: #1f2d5c;
    --ink: #2b2b2b;
    --divider: #3a3a3a;
    --on-navy: #ffffff;
    --shadow: rgba(0, 0, 0, 0.22);
  }
  * { box-sizing: border-box; margin: 0; padding: 0; }
  html, body {
    width: 1200px;
    height: 900px;
    overflow: hidden;
    background: var(--page-bg);
    font-family: "Open Sans", Arial, sans-serif;
  }
  .canvas {
    position: relative;
    width: 1200px;
    height: 900px;
  }
  .card {
    position: absolute;
    width: 580px;
    height: 330px;
    background: var(--card-white);
    box-shadow: 0 10px 28px var(--shadow);
    overflow: hidden;
  }
  .card--back { left: 90px; top: 100px; }
  .card--front { left: 530px; top: 470px; display: flex; }

  .brand {
    display: flex;
    align-items: center;
    gap: 14px;
    color: var(--navy);
    font-weight: 600;
    letter-spacing: 0.04em;
  }
  .brand__mark {
    flex: none;
    background: var(--navy);
  }
  .brand__name { line-height: 1.15; text-transform: uppercase; }

  .card--back .brand {
    position: absolute;
    left: 0; right: 0; top: 0; bottom: 0;
    justify-content: center;
  }
  .card--back .brand__mark { width: 46px; height: 46px; }
  .card--back .brand__name { font-size: 26px; }
  .card--back .brand__name small { display: block; font-size: 15px; letter-spacing: 0.08em; }

  .front__logo-side {
    width: 52%;
    display: flex;
    align-items: center;
    justify-content: center;
    border-right: 4px solid var(--divider);
  }
  .front__logo-side .brand { gap: 10px; }
  .front__logo-side .brand__mark { width: 26px; height: 26px; }
  .front__logo-side .brand__name { font-size: 17px; }
  .front__logo-side .brand__name small { display: block; font-size: 10px; letter-spacing: 0.08em; }

  .front__info {
    flex: 1;
    background: var(--navy);
    color: var(--on-navy);
    padding: 26px 18px 0 20px;
  }
  .person__name { font-size: 21px; font-weight: 700; line-height: 1.1; }
  .person__title { font-size: 12px; margin-top: 2px; }
  .address { margin-top: 32px; font-size: 12.5px; line-height: 1.45; }
  .contacts { list-style: none; margin-top: 36px; font-size: 14px; }
  .contacts li { display: flex; align-items: center; gap: 10px; margin-bottom: 7px; }
  .contacts svg { width: 12px; height: 12px; flex: none; fill: var(--on-navy); }
</style>
</head>
<body>
<main class="canvas">

  <section class="card card--back" aria-label="Card back">
    <div class="brand">
      <span class="brand__mark"></span>
      <span class="brand__name">R Marlowe<small>Management Consulting</small></span>
    </div>
  </section>

  <section class="card card--front" aria-label="Card front">
    <div class="front__logo-side">
      <div class="brand">
        <span class="brand__mark"></span>
        <span class="brand__name">R Marlowe<small>Management Consulting</small></span>
      </div>
    </div>
    <div class="front__info">
      <h1 class="person__name">Renato Marlowe</h1>
      <p class="person__title">Director General</p>
      <p class="address">Av.Dr. Morvelo Tastran, 512 - 16th floor<br>07219-316-Vila Serena-São Paulo-SP-Brazil</p>
      <ul class="contacts">
        <li>
          <svg viewBox="0 0 24 24" aria-hidden="true"><path d="M6.6 10.8a15.1 15.1 0 0 0 6.6 6.6l2.2-2.2c.3-.3.7-.4 1-.2 1.1.4 2.3.6 3.6.6.6 0 1 .4 1 1V20c0 .6-.4 1-1 1A17 17 0 0 1 3 4c0-.6.4-1 1-1h3.5c.6 0 1 .4 1 1 0 1.3.2 2.5.6 3.6.1.3 0 .7-.2 1z"/></svg>
          ++55-11-4172-8830
        </li>
        <li>
          <svg viewBox="0 0 24 24" aria-hidden="true"><path d="M7 1h10a2 2 0 0 1 2 2v18a2 2 0 0 1-2 2H7a2 2 0 0 1-2-2V3a2 2 0 0 1 2-2zm0 3v14h10V4zm5 15.5a1 1 0 1 0 0 2 1 1 0 0 0 0-2z"/></svg>
          ++55-11-93416-2057
        </li>
        <li>
          <svg viewBox="0 0 24 24" aria-hidden="true"><path d="M2 5h20v14H2zm2 2v.5l8 5 8-5V7zm0 2.8V17h16V9.8l-8 5z"/></svg>
          renato@rmarloweconsulting.com.br
        </li>
      </ul>
    </div>
  </section>

</main>
</body>
</html>
```